New company generic tri fold brochure

We are a new small business looking to reach as many potential customers as possible for a low price. We do a variety of self-defense and protection seminars that can be customized to fit the needs of church groups, corporations, community organizations, and families. We do not teach karate, we teach awareness and common self-defense movements that can be instinctively used after just a few hours of training. We believe that self-defense is not only a right, it is your responsibility.

Our preliminary seminar is called Ready for Tomorrow - This is an innovative self-defense and situational awareness personal safety training program. We focus on the predator mindset, tactics and conflict avoidance. We provide seminar attendees with our Easy, Effective, and Practical Personal Protection and life Skills tools to detect, dissuade and defeat a predator. Our goals are to teach everyone to act under extreme stress and respond instinctively using simple, real & practical everyday actions.

Our seminars do not teach “Martial Arts”. We recognize that most people don’t have the time or desire to fully embrace the concepts taught in most karate schools. The skills learned under those controlled situations will more than likely desert us in a crisis. When the body is conditioned, but not the mind, fight or flight will kick in. The bloodstream is flooded with adrenaline, vision and hearing are affected, and the mind fills with a sea of emotions. We simply can’t think normally under those circumstances. We will train you to use techniques instinctively to get you out of dangerous situations.

Everyone has the right to protect themselves and should be able to find a fun, energetic, and educational program that works with their interest, budget and time. Personal and Family protection is not an option….It’s a responsibility. Our martial art science will help you look after yourself and family. 

We also have specialized seminars for women's rape prevention, children's safety and bully handling, weapons training, personal and family protection, and professional defensive & protective procedures.

Our main professor is Carl Hoskins who has almost 40 years of learning and teaching self defense to all ages. We are in the process of setting up our website with more information and seminar dates. When it is ready for public viewing the site name is www.brightguardcourses.net. (GUARD stands for Guided Understanding And Rapid Departure).

I am attaching our main logo and some pictures we have used in the past. We prefer lighter backgrounds and royal blue lettering and accents.

Target Market(s)

Adult men and women ages 18 - 50.

Industry/Entity Type

Education

Font styles to use
Other font styles liked:
• Verdana

Colors
0455a3
ec1f27
ffffff
f04a51
3277b5
33a6d7

Requirements
Must have
• Web address - www.brightguardcourses.net
• Contact Information - Carl Hoskins - ProfessorCarl@brightguardcourses.net (208) 555-0173 and Monica Hoskins - Monica@brightguardcourses.net (208) 555-0186
• Uploaded logo. Brief description of Ready For Tomorrow with emphasis on our ability to customize the seminars to fit any family or group
Should not have
• We are trying to de-emphasize the karate aspect of self-defense. We are NOT a karate school and the seminars we teach do not require any prior knowledge of karate. We use easy to learn, simple, and instinctive moves to avoid confrontations and escape from an attacker.

```html
<!DOCTYPE html>
<html lang="en">
<head>
<meta charset="utf-8">
<title>BrightGuard Training – Tri-fold Brochure</title>
<link rel="stylesheet" href="https://fonts.googleapis.com/css2?family=Open+Sans:wght@400;600;700&display=swap">
<style>
  :root{
    --royal:#3b4ea3;
    --brick:#b13c3a;
    --steel:#1f5f97;
    --navy:#1c3b52;
    --sky:#5a9ad6;
    --white:#ffffff;
    --stage:#e9e4df;
  }
  *{box-sizing:border-box;margin:0;padding:0}
  html,body{width:1200px;height:1000px;overflow:hidden;background:var(--stage);font-family:"Open Sans",Verdana,sans-serif}
  .canvas{position:relative;width:1200px;height:1000px}
  .abs{position:absolute}
  .photo{position:absolute}

  /* inside spread */
  .inside{position:absolute;left:14px;top:12px;width:946px;height:734px;box-shadow:2px 3px 8px rgba(0,0,0,.35);overflow:hidden;background:var(--steel)}
  .inside-title{position:absolute;left:51px;top:40px;color:var(--white);font-weight:700;font-size:27px;letter-spacing:.2px}
  .copy{position:absolute;color:var(--white);font-size:13px;line-height:17.4px}
  .copy p+p{margin-top:17px}
  .copy-center{letter-spacing:.25px}
  .copy-lead{font-size:14.6px;line-height:18.2px;letter-spacing:.3px}
  .copy h3{font-weight:400;font-size:14.4px;text-decoration:underline;line-height:18px}
  .copy-group{font-size:13.8px;line-height:17.4px}

  /* outside spread */
  .outside{position:absolute;left:709px;top:611px;width:487px;height:367px;box-shadow:2px 3px 8px rgba(0,0,0,.4);overflow:hidden;background:var(--steel)}
  .small{position:absolute;color:var(--white);text-align:center}
  .brand-mark{position:absolute;display:flex;flex-direction:column;align-items:center;gap:3px}
  .brand-mark .dot{width:40px;height:40px;border-radius:50%;background:var(--white);border:2px solid var(--royal)}
  .brand-mark .name{font-size:9px;font-weight:700;color:var(--royal);text-align:center;line-height:11px;white-space:nowrap}
  .brand-mark.on-dark .name{color:var(--white);white-space:normal}
  .cover-title{position:absolute;left:310px;top:72px;width:162px;text-align:center;font-weight:700;font-size:11.5px;line-height:14px;color:var(--brick)}
  .cover-title b{color:var(--steel)}
</style>
</head>
<body>
<div class="canvas">

  <!-- INSIDE SPREAD -->
  <section class="inside">
    <svg class="abs" width="946" height="734" viewBox="0 0 946 734" style="left:0;top:0">
      <rect width="946" height="734" fill="var(--steel)"/>
      <rect x="316" y="20" width="325" height="560" fill="var(--navy)"/>
      <rect x="0" y="98" width="316" height="306" fill="var(--brick)"/>
      <rect x="0" y="578" width="316" height="130" fill="var(--brick)"/>
      <rect x="346" y="160" width="262" height="548" fill="var(--brick)"/>
      <rect x="656" y="20" width="290" height="394" fill="var(--brick)"/>
      <rect x="641" y="425" width="35" height="283" fill="var(--brick)"/>
      <polygon points="0,0 946,0 946,18 640,18 360,92 0,92" fill="var(--royal)"/>
      <polyline points="0,95 360,95 640,21 946,21" fill="none" stroke="var(--sky)" stroke-width="4"/>
      <rect x="0" y="708" width="946" height="26" fill="var(--royal)"/>
    </svg>

    <h1 class="inside-title">Professor Carl</h1>

    <div class="photo" role="img" aria-label="Photo of Professor Carl standing by a white car" style="left:51px;top:103px;width:223px;height:270px;background:linear-gradient(160deg,#7d8a6e,#9aa6a8 45%,#4a4a44)"></div>
    <div class="copy" style="left:51px;top:430px;width:222px">My wife, Monica, and I established BrightGuard Training as a positive way to use my 39 years of Martial Arts, personal protection training and knowledge to reach as many people both casual and professional, as possible.</div>
    <div class="photo" role="img" aria-label="Silhouette figures demonstrating self-defense moves" style="left:8px;top:598px;width:295px;height:110px;background:linear-gradient(90deg,#f2eeee,#e6dede)"></div>

    <div class="photo" role="img" aria-label="Photo of an attacker grabbing a woman's handbag" style="left:386px;top:73px;width:154px;height:102px;background:linear-gradient(120deg,#c9b6a8,#3e3a3a 60%,#e8e4e0)"></div>
    <div class="copy copy-center" style="left:365px;top:215px;width:224px">
      <p>Ready for Tomorrow is an innovative self-defense and situational awareness personal safety training program. We focus on the predator mindset, tactics and conflict avoidance. We provide seminar attendees with our Easy, Effective, and Practical Personal Protection and Life skills to detect, dissuade, and defeat a predator.</p>
      <p>Our goals are to teach everyone to act under extreme stress and respond instinctively using simple, real &amp; practical everyday actions.</p>
      <p>Our seminars do not teach “Martial Arts”. We recognize that most people don’t have the time or desire to fully embrace the concept taught in most karate schools. The skills learned under those controlled situations will most likely desert us in a crisis. We will train you to use techniques instinctively to get you out of dangerous situations.</p>
    </div>

    <div class="copy copy-lead" style="left:676px;top:70px;width:232px">Empower yourself and attain a higher level of self-confidence with this one-of-a-kind <i>personal</i> protection or weapon seminars that will teach you life-saving skills. All courses provide hands-on training courses that can be easily learned in a few short hours.</div>
    <div class="photo" role="img" aria-label="Silhouette of a woman defending herself from an attacker" style="left:676px;top:248px;width:223px;height:147px;background:linear-gradient(90deg,#f4f4f4,#d8d8d8 50%,#f4f4f4)"></div>

    <div class="copy copy-group" style="left:679px;top:428px;width:226px">
      <h3>Group Safety Training</h3>
      BrightGuard Training is happy to work with you to customize our content to fit your audience’s needs whether you are a small business, University, Corporation, or religious organization for men and/or women. We focus on conflict avoidance and you will learn practical skills.
    </div>
  </section>

  <!-- OUTSIDE SPREAD -->
  <section class="outside">
    <svg class="abs" width="487" height="367" viewBox="0 0 487 367" style="left:0;top:0">
      <rect width="487" height="367" fill="var(--steel)"/>
      <polygon points="0,228 160,228 160,367 0,367" fill="var(--brick)"/>
      <polygon points="160,20 306,20 306,367 160,367" fill="var(--brick)"/>
      <polygon points="160,160 306,40 306,367 160,367" fill="var(--steel)"/>
      <polygon points="170,340 190,340 306,150 306,95" fill="var(--sky)"/>
      <polygon points="0,20 160,20 160,118 0,118" fill="var(--brick)"/>
      <rect x="306" y="20" width="168" height="104" fill="var(--white)"/>
      <rect x="306" y="124" width="168" height="243" fill="var(--brick)"/>
      <rect x="312" y="186" width="156" height="164" fill="var(--steel)"/>
      <polygon points="0,0 487,0 487,14 306,14 160,34 0,34" fill="var(--royal)"/>
      <polyline points="0,37 160,37 306,17 487,17" fill="none" stroke="var(--sky)" stroke-width="3"/>
      <rect x="0" y="352" width="487" height="15" fill="var(--royal)"/>
    </svg>

    <div class="photo" role="img" aria-label="Photo of instructor and student sitting on a large rock" style="left:12px;top:18px;width:133px;height:95px;background:linear-gradient(140deg,#5e7a3e,#8a8a6a 50%,#4c6030)"></div>
    <div class="photo" role="img" aria-label="Photo of Professor Carl with a dog" style="left:165px;top:18px;width:135px;height:95px;background:linear-gradient(140deg,#7a6a52,#3a3430 55%,#a0906e)"></div>
    <div class="small" style="left:10px;top:150px;width:140px;font-size:7.4px;line-height:9.6px">Our award-winning self-defense techniques are proven to be effective against a wide variety of predators. Join us today to learn how to protect yourself, your family, and your home.</div>
    <div class="photo" role="img" aria-label="Photo of a family gathered at an open car trunk" style="left:12px;top:242px;width:133px;height:93px;background:linear-gradient(140deg,#6a7048,#b8a48a 50%,#8a6a5a)"></div>

    <div class="brand-mark on-dark" style="left:190px;top:150px;width:80px">
      <span class="dot"></span>
      <span class="name">BrightGuard Training LLC</span>
    </div>
    <div class="small" style="left:162px;top:275px;width:140px;font-size:6.6px;line-height:8.6px">
      BrightGuard Training LLC<br>PO Box 4418<br>Boise, ID 83702<br><br>Phone - (208) 555-0173<br>www.brightguardcourses.net<br>ProfessorCarl@brightguardcourses.net
    </div>

    <div class="brand-mark" style="left:316px;top:14px;width:148px">
      <span class="dot"></span>
      <span class="name">BrightGuard Training LLC</span>
    </div>
    <div class="cover-title"><b>G</b>uided <b>U</b>nderstanding <b>A</b>nd <b>R</b>apid <b>D</b>eparture</div>
    <div class="small" style="left:312px;top:131px;width:156px;font-size:11px;line-height:13.6px">Realistic &amp; Effective Self-Defense for Personal and Family Safety</div>
    <div class="small" style="left:316px;top:194px;width:148px;font-size:8.6px;line-height:11px">Taught by Professor Carl Hoskins, Idaho’s Leading Personal Safety Expert</div>
    <div class="photo" role="img" aria-label="Photo of instructor and student sitting on a rock in a garden" style="left:322px;top:244px;width:136px;height:88px;background:linear-gradient(140deg,#5e7a3e,#8a8a6a 50%,#4c6030)"></div>
    <div class="small" style="left:314px;top:335px;width:152px;font-size:5.6px;line-height:6.6px">Self-defense is not only a right,<br>it’s your responsibility.</div>
  </section>

</div>
</body>
</html>
```